Modified Business card

We have developed a new logo for the business, and want thou to tray and incorporate it into the business card design that you have done for us.

I am going to upload the logo files. We like the simple clean look that you have on the card, so if you can keep the look incorporating the logo.

Industry/Entity Type

Business

```html
<!DOCTYPE html>
<html lang="en">
<head>
<meta charset="utf-8">
<title>Corvane Engineering – Business Card</title>
<link rel="stylesheet" href="https://fonts.googleapis.com/css2?family=Ubuntu:wght@400;500;700&display=swap">
<style>
  :root {
    --stage: #2b2b2d;
    --brand-red: #c8161d;
    --brand-red-dark: #8e0f14;
    --ink: #3a3a3c;
    --ink-soft: #555558;
    --stripe: #111111;
    --paper: #ffffff;
    --paper-shade: #e4e4e6;
  }
  * { box-sizing: border-box; margin: 0; padding: 0; }
  html, body { width: 1200px; height: 900px; overflow: hidden; }
  body {
    background: var(--stage);
    font-family: "Ubuntu", Arial, sans-serif;
    position: relative;
  }
  .card {
    position: absolute;
    left: 300px;
    width: 600px;
    height: 343px;
    border-radius: 8px;
    overflow: hidden;
    box-shadow: 0 10px 30px rgba(0,0,0,.45);
  }

  /* Back of card */
  .card-back {
    top: 80px;
    background: radial-gradient(ellipse at 40% 40%, #d81c23 0%, var(--brand-red) 45%, var(--brand-red-dark) 100%);
  }
  .card-back .wordmark {
    position: absolute;
    left: 150px;
    top: 138px;
    display: flex;
    align-items: center;
    gap: 14px;
  }
  .card-back .wordmark-square {
    width: 46px; height: 46px;
    background: var(--paper);
    border-radius: 6px;
  }
  .card-back .wordmark-name {
    color: var(--paper);
    font-weight: 700;
    font-size: 30px;
    letter-spacing: .5px;
  }
  .card-back .web {
    position: absolute;
    left: 210px;
    top: 196px;
    color: var(--paper);
    font-size: 14px;
    font-weight: 500;
  }

  /* Front of card */
  .card-front {
    top: 477px;
    background: linear-gradient(160deg, var(--paper) 0%, #f3f3f4 55%, var(--paper-shade) 100%);
  }
  .card-front .swoosh { position: absolute; inset: 0; }
  .card-front .wordmark {
    position: absolute;
    right: 40px;
    top: 30px;
    display: flex;
    align-items: center;
    gap: 14px;
  }
  .card-front .wordmark-square {
    width: 50px; height: 50px;
    background: var(--brand-red);
    border-radius: 6px;
  }
  .card-front .wordmark-name {
    color: var(--ink);
    font-weight: 700;
    font-size: 30px;
    letter-spacing: .5px;
  }
  .person {
    position: absolute;
    left: 40px;
    top: 140px;
    color: var(--ink);
  }
  .person-name { font-size: 24px; font-weight: 700; }
  .person-credentials { font-size: 16px; color: var(--ink-soft); margin-top: 4px; }
  .person-role { font-size: 16px; color: var(--ink-soft); margin-top: 14px; }

  .contacts {
    position: absolute;
    left: 330px;
    top: 96px;
    list-style: none;
    font-size: 13px;
    color: var(--ink);
    line-height: 17px;
  }
  .contacts li { display: flex; align-items: flex-start; gap: 8px; }
  .contacts svg { width: 13px; height: 13px; flex: none; margin-top: 2px; }
  .contacts .icon { fill: var(--brand-red); stroke: none; }
</style>
</head>
<body>

<section class="card card-back">
  <div class="wordmark">
    <span class="wordmark-square"></span>
    <span class="wordmark-name">Corvane Engineering</span>
  </div>
  <div class="web">www.corvane.co.za</div>
</section>

<section class="card card-front">
  <svg class="swoosh" viewBox="0 0 600 343" preserveAspectRatio="none" aria-hidden="true">
    <path d="M0 262 C 200 262, 420 250, 600 218 L600 230 C 420 262, 200 274, 0 274 Z" fill="var(--stripe)"/>
    <path d="M0 280 C 200 280, 420 268, 600 236 L600 343 L0 343 Z" fill="var(--brand-red)"/>
  </svg>

  <div class="wordmark">
    <span class="wordmark-square"></span>
    <span class="wordmark-name">Corvane Engineering</span>
  </div>

  <div class="person">
    <div class="person-name">Dorian Kessler</div>
    <div class="person-credentials">M.Sc Eng, C.Eng</div>
    <div class="person-role">CEO</div>
  </div>

  <ul class="contacts">
    <li>
      <svg viewBox="0 0 16 16"><path class="icon" d="M8 0a5 5 0 0 0-5 5c0 4 5 11 5 11s5-7 5-11a5 5 0 0 0-5-5zm0 7a2 2 0 1 1 0-4 2 2 0 0 1 0 4z"/></svg>
      <span>14 Marlow Rd Seaview<br>7950 South Africa</span>
    </li>
    <li>
      <svg viewBox="0 0 16 16"><path class="icon" d="M4 0h8a1 1 0 0 1 1 1v14a1 1 0 0 1-1 1H4a1 1 0 0 1-1-1V1a1 1 0 0 1 1-1zm1 2v10h6V2z"/></svg>
      <span>+27 (0) 82 555 0142</span>
    </li>
    <li>
      <svg viewBox="0 0 16 16"><path class="icon" d="M1 5h14v9H1zM4 1h8v3H4zm0 7v2h3V8zm5 0v2h3V8z"/></svg>
      <span>+27 (0) 86 555 0178</span>
    </li>
    <li>
      <svg viewBox="0 0 16 16"><path class="icon" d="M0 3h16v10H0zm1.5 1.5L8 9l6.5-4.5V4L8 8 1.5 4z"/></svg>
      <span>dorian.kessler@corvane.co.za</span>
    </li>
    <li>
      <svg viewBox="0 0 16 16"><path class="icon" d="M8 0a8 8 0 1 0 0 16A8 8 0 0 0 8 0zm0 2a6 6 0 0 1 5.7 4H2.3A6 6 0 0 1 8 2zM2 8l.1-1h11.8l.1 1-.1 1H2.1zm.3 2h11.4A6 6 0 0 1 2.3 10z"/></svg>
      <span>www.corvane.co.za</span>
    </li>
  </ul>
</section>

</body>
</html>
```